Boutique town planning business needs a Business Card design

We need a business card design for a new company called The Zoning Bridgeway. We provide town planning and urban design services to government, business and community groups. We would like to see the designs use the colours in the logo (blue, deep red, green and amber), plenty of white and including black and grey in the writing. The final design should communicate collaboration, creativity and professionalism and that we are approachable.

```html
<!DOCTYPE html>
<html lang="en">
<head>
<meta charset="utf-8">
<title>The Zoning Bridgeway – Business Card</title>
<link href="https://fonts.googleapis.com/css2?family=Open+Sans:wght@400;600;700&display=swap" rel="stylesheet">
<style>
  :root {
    --red: #a8322a;
    --blue: #4ea3cf;
    --green: #6aa842;
    --amber: #eaa020;
    --ink: #1f1f1f;
    --grey: #5e5e5e;
    --paper: #ffffff;
    --backdrop: #e9e9e7;
  }
  * { box-sizing: border-box; margin: 0; padding: 0; }
  html, body {
    width: 1200px;
    height: 896px;
    overflow: hidden;
    background: var(--backdrop);
    font-family: "Open Sans", Arial, sans-serif;
    color: var(--ink);
  }
  .canvas {
    position: relative;
    width: 1200px;
    height: 896px;
    display: flex;
    align-items: center;
    justify-content: center;
    gap: 40px;
  }
  .card {
    position: relative;
    width: 540px;
    height: 330px;
    background: var(--paper);
    box-shadow: 0 2px 10px rgba(0,0,0,0.12);
    overflow: hidden;
  }

  /* Contact side */
  .brand {
    position: absolute;
    display: flex;
    align-items: center;
    gap: 10px;
  }
  .brand-name {
    font-weight: 700;
    color: var(--grey);
    line-height: 1.05;
  }
  .brand-dot {
    border-radius: 50%;
    background: var(--grey);
    flex: none;
  }
  .contact .brand { left: 34px; top: 30px; }
  .contact .brand-name { font-size: 21px; }
  .contact .brand-dot { width: 16px; height: 16px; }

  .person {
    position: absolute;
    right: 34px;
    top: 34px;
    text-align: right;
  }
  .person-name {
    font-size: 25px;
    font-weight: 400;
    color: var(--red);
    line-height: 1.2;
  }
  .person-role {
    font-size: 17px;
    color: var(--ink);
  }

  .details {
    position: absolute;
    top: 150px;
    list-style: none;
    font-size: 13.5px;
    color: var(--ink);
  }
  .details li {
    display: flex;
    align-items: center;
    gap: 8px;
    height: 24px;
  }
  .details svg { width: 13px; height: 13px; flex: none; fill: var(--ink); }
  .details-left { left: 34px; }
  .details-right { left: 250px; }

  .colour-band {
    position: absolute;
    left: 0; right: 0; bottom: 0;
    height: 34px;
    display: flex;
  }
  .colour-band span { flex: 1; }
  .band-red { background: var(--red); }
  .band-blue { background: var(--blue); }
  .band-green { background: var(--green); }
  .band-amber { background: var(--amber); }

  /* Brand side */
  .front {
    display: flex;
    align-items: center;
    justify-content: center;
  }
  .front .brand { position: static; gap: 18px; }
  .front .brand-name { font-size: 34px; }
  .front .brand-dot { width: 64px; height: 64px; }
</style>
</head>
<body>
<main class="canvas">

  <section class="card contact" aria-label="Business card, contact side">
    <div class="brand">
      <p class="brand-name">The Zoning<br>Bridgeway</p>
      <span class="brand-dot"></span>
    </div>

    <div class="person">
      <p class="person-name">Maren Ashcroft</p>
      <p class="person-role">Director</p>
    </div>

    <ul class="details details-left">
      <li>
        <svg viewBox="0 0 24 24" aria-hidden="true"><path d="M6.6 10.8a15.1 15.1 0 0 0 6.6 6.6l2.2-2.2a1 1 0 0 1 1-.25 11.4 11.4 0 0 0 3.6.57 1 1 0 0 1 1 1V20a1 1 0 0 1-1 1A17 17 0 0 1 3 4a1 1 0 0 1 1-1h3.5a1 1 0 0 1 1 1c0 1.25.2 2.45.57 3.6a1 1 0 0 1-.25 1z"/></svg>
        ABN 12 345 678 901
      </li>
      <li>
        <svg viewBox="0 0 24 24" aria-hidden="true"><path d="M6.6 10.8a15.1 15.1 0 0 0 6.6 6.6l2.2-2.2a1 1 0 0 1 1-.25 11.4 11.4 0 0 0 3.6.57 1 1 0 0 1 1 1V20a1 1 0 0 1-1 1A17 17 0 0 1 3 4a1 1 0 0 1 1-1h3.5a1 1 0 0 1 1 1c0 1.25.2 2.45.57 3.6a1 1 0 0 1-.25 1z"/></svg>
        0412 555 318
      </li>
    </ul>

    <ul class="details details-right">
      <li>
        <svg viewBox="0 0 24 24" aria-hidden="true"><path d="M2 5h20v14H2z M3.5 6.5 12 13l8.5-6.5" fill="none" stroke="#1f1f1f" stroke-width="2"/></svg>
        thezoningbridgeway@mailbox.com
      </li>
      <li>
        <svg viewBox="0 0 24 24" aria-hidden="true"><g fill="none" stroke="#1f1f1f" stroke-width="2"><circle cx="12" cy="12" r="10"/><path d="M2 12h20M12 2c3 3 3 17 0 20M12 2c-3 3-3 17 0 20"/></g></svg>
        www.thezoningbridgeway.com.au
      </li>
    </ul>

    <div class="colour-band" aria-hidden="true">
      <span class="band-red"></span>
      <span class="band-blue"></span>
      <span class="band-green"></span>
      <span class="band-amber"></span>
    </div>
  </section>

  <section class="card front" aria-label="Business card, brand side">
    <div class="brand">
      <p class="brand-name">The Zoning<br>Bridgeway</p>
      <span class="brand-dot"></span>
    </div>
  </section>

</main>
</body>
</html>
```